Diagram of Tallowmere’s history for website

This project is to design the attached diagram along the lines of the attached image but in our branding - style guide attached. The diagram will be going on the Tallowmere website - www.tallowmere.au.

```html
<!DOCTYPE html>
<html lang="en">
<head>
<meta charset="utf-8">
<title>Tallowmere – Our History</title>
<link rel="stylesheet" href="https://fonts.googleapis.com/css2?family=Poppins:wght@400;700&display=swap">
<style>
  :root {
    --ink: #333333;
    --green: #6f8f74;
    --blue: #7f9ea3;
    --peach: #d4aa96;
    --frame: #dddddd;
    --chev-grey: #a9a9a9;
    --chev-blue: #c8d5d7;
    --chev-green: #c1cfc3;
    --chev-peach: #ecd9d1;
    --paper: #ffffff;
  }
  html, body {
    margin: 0;
    width: 1200px;
    height: 1200px;
    overflow: hidden;
    background: var(--paper);
  }
  .history-diagram { display: block; width: 1200px; height: 1200px; }
  .history-diagram text { font-family: "Poppins", sans-serif; }
  .title { font-size: 52px; font-weight: 400; fill: var(--ink); }
  .year { font-size: 58px; font-weight: 700; letter-spacing: -1px; }
  .heading { font-size: 26px; font-weight: 700; }
  .body-copy { font-size: 11px; font-weight: 400; fill: var(--ink); }
  .is-green { fill: var(--green); }
  .is-blue { fill: var(--blue); }
  .is-peach { fill: var(--peach); }
  .stem { stroke-width: 5; fill: none; }
  .stem-green { stroke: var(--green); }
  .stem-blue { stroke: var(--blue); }
  .stem-peach { stroke: var(--peach); }
  .axis-dot { stroke: var(--paper); stroke-width: 3; }
  .axis-line { stroke: var(--ink); stroke-width: 16; }
</style>
</head>
<body>
<svg class="history-diagram" viewBox="0 0 1920 1920" xmlns="http://www.w3.org/2000/svg" role="group" aria-label="Tallowmere history timeline 2017 to 2023">
  <rect class="panel-frame" x="135" y="491" width="1662" height="950" fill="var(--paper)" stroke="var(--frame)" stroke-width="1.5"/>

  <g class="chevrons">
    <polygon points="153,513 190,513 213,551 190,590 153,590 176,551" fill="var(--chev-grey)"/>
    <polygon points="217,513 254,513 277,551 254,590 217,590 240,551" fill="var(--chev-blue)"/>
    <polygon points="281,513 318,513 341,551 318,590 281,590 304,551" fill="var(--chev-green)"/>
    <polygon points="345,513 382,513 405,551 382,590 345,590 368,551" fill="var(--chev-peach)"/>
  </g>

  <text class="title" x="965" y="557" text-anchor="middle">Our History</text>

  <!-- stems -->
  <line class="stem stem-green" x1="194" y1="1004" x2="194" y2="1240"/>
  <line class="stem stem-blue" x1="450" y1="826" x2="450" y2="985"/>
  <line class="stem stem-peach" x1="705" y1="1020" x2="705" y2="1100"/>
  <line class="stem stem-green" x1="961" y1="827" x2="961" y2="985"/>
  <line class="stem stem-blue" x1="1212" y1="1020" x2="1212" y2="1330"/>
  <line class="stem stem-peach" x1="1468" y1="594" x2="1468" y2="985"/>

  <!-- axis -->
  <line class="axis-line" x1="194" y1="1004" x2="1716" y2="1004"/>
  <polygon points="1712,982 1750,1004 1712,1025" fill="var(--ink)"/>

  <circle class="axis-dot" cx="194" cy="1004" r="19" fill="var(--green)"/>
  <circle class="axis-dot" cx="450" cy="1004" r="19" fill="var(--blue)"/>
  <circle class="axis-dot" cx="705" cy="1004" r="19" fill="var(--peach)"/>
  <circle class="axis-dot" cx="961" cy="1004" r="19" fill="var(--green)"/>
  <circle class="axis-dot" cx="1212" cy="1004" r="19" fill="var(--blue)"/>
  <circle class="axis-dot" cx="1468" cy="1004" r="19" fill="var(--peach)"/>

  <!-- milestone dots -->
  <g class="milestone-dots">
    <circle cx="194" cy="1109" r="11" fill="var(--green)"/>
    <circle cx="194" cy="1247" r="11" fill="var(--green)"/>
    <circle cx="450" cy="826" r="11" fill="var(--blue)"/>
    <circle cx="705" cy="1111" r="11" fill="var(--peach)"/>
    <circle cx="961" cy="827" r="11" fill="var(--green)"/>
    <circle cx="1212" cy="1111" r="11" fill="var(--blue)"/>
    <circle cx="1212" cy="1226" r="11" fill="var(--blue)"/>
    <circle cx="1212" cy="1336" r="11" fill="var(--blue)"/>
    <circle cx="1468" cy="594" r="11" fill="var(--peach)"/>
    <circle cx="1468" cy="686" r="11" fill="var(--peach)"/>
    <circle cx="1468" cy="786" r="11" fill="var(--peach)"/>
    <circle cx="1468" cy="876" r="11" fill="var(--peach)"/>
  </g>

  <!-- 2017 -->
  <g class="year-2017">
    <text class="year is-green" x="214" y="1073">2017</text>
    <text class="heading is-green" x="217" y="1110">Tallowmere</text>
    <text class="heading is-green" x="217" y="1132">Commences</text>
    <text class="body-copy" x="217" y="1158">Maren started the business with 25 years’</text>
    <text class="body-copy" x="217" y="1175">experience working for government &amp; non-</text>
    <text class="body-copy" x="217" y="1193">government disability &amp; community</text>
    <text class="body-copy" x="217" y="1210">services. Our first office is in Preston.</text>
    <text class="heading is-green" x="217" y="1262">NDIS Provider</text>
    <text class="body-copy" x="217" y="1289">Tallowmere becomes a NDIS Registered</text>
    <text class="body-copy" x="217" y="1306">provider</text>
  </g>

  <!-- 2018 -->
  <g class="year-2018">
    <text class="heading is-blue" x="473" y="831">Clinic</text>
    <text class="heading is-blue" x="473" y="853">Expansion</text>
    <text class="body-copy" x="473" y="880">Tallowmere moves offices twice in Preston</text>
    <text class="body-copy" x="473" y="897">due to growth &amp; expansion. Clinic</text>
    <text class="body-copy" x="473" y="914">established</text>
    <text class="year is-blue" x="471" y="980">2018</text>
  </g>

  <!-- 2019 -->
  <g class="year-2019">
    <text class="year is-peach" x="725" y="1073">2019</text>
    <text class="heading is-peach" x="728" y="1110">Move to</text>
    <text class="heading is-peach" x="728" y="1132">Alphington</text>
    <text class="body-copy" x="730" y="1158">Tallowmere moves to Alphington due to</text>
    <text class="body-copy" x="728" y="1175">further growth &amp; expansion</text>
  </g>

  <!-- 2021 -->
  <g class="year-2021">
    <text class="heading is-green" x="985" y="836">Impact-Corporation</text>
    <text class="body-copy" x="985" y="862">Tallowmere becomes a accredited Impact-</text>
    <text class="body-copy" x="985" y="879">Corporation having met the highest</text>
    <text class="body-copy" x="985" y="897">standards of environmental, social &amp;</text>
    <text class="body-copy" x="985" y="914">community performance</text>
    <text class="year is-green" x="984" y="980">2021</text>
  </g>

  <!-- 2022 -->
  <g class="year-2022">
    <text class="year is-blue" x="1234" y="1073">2022</text>
    <text class="heading is-blue" x="1237" y="1110">Corvana Best</text>
    <text class="heading is-blue" x="1237" y="1132">of Business</text>
    <text class="body-copy" x="1237" y="1158">Tallowmere wins the Corvana Best of Business</text>
    <text class="body-copy" x="1237" y="1175">Award (Vic) for building communities</text>
    <text class="heading is-blue" x="1237" y="1228">Move to</text>
    <text class="heading is-blue" x="1237" y="1250">Coburg</text>
    <text class="body-copy" x="1239" y="1275">Tallowmere moves to a larger premises in</text>
    <text class="body-copy" x="1237" y="1292">Coburg</text>
    <text class="heading is-blue" x="1237" y="1346">Partnerships</text>
    <text class="body-copy" x="1237" y="1371">Partnerships established with Lagoon Bay</text>
    <text class="body-copy" x="1237" y="1389">School for Children with Disability &amp;</text>
    <text class="body-copy" x="1237" y="1406">Wattle Circle (Southgate University</text>
  </g>

  <!-- 2023 -->
  <g class="year-2023">
    <text class="heading is-peach" x="1493" y="608">Rebranding</text>
    <text class="body-copy" x="1495" y="635">Tallowmere rebranded</text>
    <text class="heading is-peach" x="1493" y="687">Reconciliation</text>
    <text class="heading is-peach" x="1493" y="709">Action Plan (RAP)</text>
    <text class="body-copy" x="1493" y="735">Tallowmere’s Reflect RAP developed &amp; endorsed</text>
    <text class="heading is-peach" x="1493" y="787">E-Learning</text>
    <text class="heading is-peach" x="1493" y="809">Platform</text>
    <text class="body-copy" x="1493" y="836">Tallowmere e-learning platform launced</text>
    <text class="heading is-peach" x="1493" y="887">Pride Seal</text>
    <text class="body-copy" x="1493" y="914">Tallowmere achieves Pride Seal accreditation</text>
    <text class="year is-peach" x="1490" y="980">2023</text>
  </g>
</svg>
</body>
</html>
```